Consumer Protection Law Firm Needs a New Website

We need a new website for our law firm. We practice consumer protection law, with an emphasis on class actions. In particular, we serve consumers who are harassed by telemarketers, debt collectors, abusive companies, and financial criminals. In short, we sue big companies that do bad things to lots of people.

The lawyer is Tomas Fenwald. Current website is available through www.FenwaldLegal.example. Some logo files are attached.

Prefer designs that use the colors black, red, and white, per the logo. Also prefer clean, lightweight HTML5/CSS3 design rather than Wordpress. Finally, single-page type design preferred over multi-page, but flexible.

I have some limited familiarity with HTML and CSS, particularly Bootstrap, so a Bootstrap type design that I can modify myself would be ideal.

Target Market(s)

Consumers with cellular telephones.

Industry/Entity Type

Law Firm

Coding

Coded - Design and coding required

Number of Pages Required

1 page

Requirements
Must have
• - Mobile friendly, preferably without requiring separate design. In other words, a framework like Bootstrap is preferred.
• - Contact Form
• - A section for recent results
• - A section for a picture and bio of Tomas Fenwald, Esq.
Nice to have
• - Animated elements that count-up and populate with numbers for things like:
• * X dollars recovered for consumers.
• * Y clients represented
• * Over Z lawsuits filed for consumers

```html
<!DOCTYPE html>
<html lang="en">
<head>
<meta charset="utf-8">
<title>Fenwald Legal – Consumer Advocates</title>
<link href="https://fonts.googleapis.com/css2?family=Open+Sans:wght@400;600;700&family=Roboto:wght@300;700&display=swap" rel="stylesheet">
<style>
:root{
  --red:#b3052a;
  --ink:#2a2a30;
  --topbar:#2b2b31;
  --navbar:#dcdce0;
  --hero-a:#e9e9ec;
  --hero-b:#c9c9ce;
  --scrim:rgba(22,22,28,.6);
  --field-line:#d9d9d9;
  --placeholder:#8a8a8a;
}
*{box-sizing:border-box;margin:0;padding:0}
html,body{width:1200px;height:751px;overflow:hidden}
body{position:relative;font-family:"Open Sans",sans-serif;background:var(--hero-b)}
.hero-photo{position:absolute;inset:0;background:linear-gradient(100deg,var(--hero-a) 0%,#dedee2 45%,var(--hero-b) 75%,#b9b8bc 100%)}
.topbar{position:absolute;left:0;top:0;width:100%;height:27px;background:var(--topbar);color:#e6e6e6;font-size:10.5px}
.topbar .item{position:absolute;top:7px;display:flex;align-items:center;gap:8px}
.topbar .mail{left:798px}
.topbar .phone{left:952px;font-weight:700}
.navbar{position:absolute;left:0;top:27px;width:100%;height:49px;background:var(--navbar)}
.brand{position:absolute;left:161px;top:13px;height:77px;display:flex;align-items:center;gap:10px;padding:0 14px;background:#fff;border-radius:8px}
.brand-mark{width:40px;height:40px;background:var(--red)}
.brand-name{font-size:21px;font-weight:400;color:var(--ink);letter-spacing:1px;white-space:nowrap}
.nav{position:absolute;top:47px;font-size:10.5px;color:var(--ink);letter-spacing:.2px}
.nav.active{color:var(--red)}
.hero-copy{position:absolute;left:161px;top:238px;color:#fff}
.hero-copy h1{font-family:"Roboto",sans-serif;font-size:34px;line-height:40.5px;font-weight:300;white-space:nowrap}
.hero-copy h1 strong{font-weight:700}
.hero-copy p{margin-top:30px;width:540px;font-size:13.5px;line-height:22.5px;color:#f4f4f4}
.cta{position:absolute;left:161px;top:496px;width:278px;height:52px;background:var(--red);color:#fff;font-weight:700;font-size:13.5px;display:flex;align-items:center;justify-content:center;letter-spacing:.2px}
.scrim{position:absolute;inset:0;background:var(--scrim)}
.modal{position:absolute;left:461px;top:235px;width:278px;height:340px;background:#fff;border-radius:6px}
.modal .close{position:absolute;left:252px;top:8px}
.modal h2{position:absolute;left:37px;top:28px;font-family:"Roboto",sans-serif;font-weight:700;font-size:21.5px;color:#222;white-space:nowrap}
.field{position:absolute;left:36px;width:203px;border:1px solid var(--field-line);font-size:10.5px;color:var(--placeholder);padding:8px 9px}
.field.name{top:63px;height:30px}
.field.email{top:96px;height:30px}
.field.phone{top:129px;height:30px}
.field.message{top:162px;height:98px;padding-top:10px}
.send{position:absolute;left:36px;top:264px;width:203px;height:45px;background:var(--red);color:#fff;font-size:10.5px;font-weight:700;display:flex;align-items:center;justify-content:center}
</style>
</head>
<body>
<div class="hero-photo" role="img" aria-label="Soft-focus office scene with a person holding a smartphone showing a warning message"></div>

<header>
  <div class="topbar">
    <span class="item mail">
      <svg width="10" height="8" viewBox="0 0 10 8"><rect width="10" height="8" rx="1" fill="#e6e6e6"/><path d="M0 1l5 3.5L10 1" stroke="#2b2b31" fill="none"/></svg>
      info@fenwaldlegal.example
    </span>
    <span class="item phone">
      <svg width="9" height="9" viewBox="0 0 10 10"><path d="M2 0l2 2.5-1.2 1.3a6 6 0 003.4 3.4L7.5 6 10 8l-1.5 2C4 10 0 6 0 1.5z" fill="#e6e6e6"/></svg>
      855-FENWALD
    </span>
  </div>
  <div class="navbar">
    <span class="nav active" style="left:634px;top:20px">HOME</span>
    <span class="nav" style="left:695px;top:20px">ABOUT US</span>
    <span class="nav" style="left:777px;top:20px">PRACTICE AREAS</span>
    <span class="nav" style="left:890px;top:20px">LOCATION</span>
    <span class="nav" style="left:973px;top:20px">CONTACT US</span>
  </div>
  <div class="brand"><span class="brand-mark"></span><span class="brand-name">FENWALD LEGAL</span></div>
</header>

<main>
  <section class="hero-copy">
    <h1><strong>TELEPHONE HARASSMENT</strong><br>IS A SERIOUS VIOLATION OF<br>YOUR RIGHTS.</h1>
    <p>Tomas Fenwald is a consumer lawyer dedicated to helping victims of telephone harassment and debt collection abuse. Have you been harassed? Don't delay, contact us today.</p>
  </section>
  <a class="cta">GET YOUR FREE CONSULTATION</a>
</main>

<div class="scrim"></div>

<div class="modal" role="dialog" aria-label="Free consultation">
  <svg class="close" width="18" height="18" viewBox="0 0 18 18"><circle cx="9" cy="9" r="8" fill="#fff" stroke="#b3052a" stroke-width="1.5"/><path d="M6 6l6 6M12 6l-6 6" stroke="#b3052a" stroke-width="2.2" stroke-linecap="round"/></svg>
  <h2>FREE CONSULTATION</h2>
  <div class="field name">Name</div>
  <div class="field email">Email</div>
  <div class="field phone">Phone</div>
  <div class="field message">Message</div>
  <div class="send">SEND MESSAGE</div>
</div>
</body>
</html>
```